Airport Advertising Brochure

I need a flyer put together asap! Previous example included. Would like something clean and updated. New logo and updated company name. I would like this designed in Pages or Illustrator so I can update content when needed. Website: pagelantern.com

Target Market(s)

Authors. This page has some good content about what we do: https://www.pagelantern.com/terminaladvertising/

Industry/Entity Type

Airport

Font styles to use
Serif
Sans Serif

Requirements
Must have
• Clean, modern design.

```html
<!DOCTYPE html>
<html lang="en">
<head>
<meta charset="utf-8">
<title>PageLantern – Terminal Advertising Flyers</title>
<link href="https://fonts.googleapis.com/css2?family=Lato:wght@300;400;700&display=swap" rel="stylesheet">
<style>
  :root{
    --stage:#a5a5a5;
    --paper:#ffffff;
    --paper-shade:#e9e9e9;
    --ink:#161616;
    --ink-soft:#333333;
    --accent:#fcd90f;
    --photo-warm:#b48a5c;
    --photo-cool:#c9cdd2;
    --photo-deep:#5a4030;
  }
  html,body{margin:0;padding:0;width:1200px;height:1200px;overflow:hidden;background:var(--stage);}
  .stage{position:relative;width:1200px;height:1200px;}
  .flyer{position:absolute;width:523px;height:391px;box-shadow:4px 5px 8px rgba(0,0,0,.35);background:var(--paper);}
  .flyer svg{display:block;width:100%;height:100%;}
  .flyer--overview{left:46px;top:192px;}
  .flyer--window{left:632px;top:192px;}
  .flyer--table{left:306px;top:642px;}
  text{font-family:'Lato',sans-serif;fill:var(--ink);}
  .t-light{font-weight:300;}
  .t-bold{font-weight:700;}
  .t-accent{fill:var(--accent);}
  .t-body{font-size:12px;fill:var(--ink-soft);}
  .t-small{font-size:10.5px;fill:var(--ink-soft);}
  .brand{font-size:17px;font-weight:400;fill:var(--ink-soft);}
  .accent-fill{fill:var(--accent);}
  .ink-fill{fill:var(--ink);}
  .accent-line{fill:none;stroke:var(--accent);stroke-width:4;}
  .ink-line{fill:none;stroke:var(--ink);stroke-width:3;}
  .icon{fill:none;stroke:var(--ink-soft);stroke-width:1.2;}
</style>
</head>
<body>
<div class="stage">

  <!-- Overview flyer -->
  <div class="flyer flyer--overview">
    <svg viewBox="0 0 654 489" xmlns="http://www.w3.org/2000/svg">
      <defs>
        <linearGradient id="paperGrad" x1="0" y1="0" x2="1" y2="1">
          <stop offset="0" stop-color="#ffffff"/><stop offset="1" stop-color="#e6e6e6"/>
        </linearGradient>
        <linearGradient id="terminalGrad" x1="0" y1="0" x2="0" y2="1">
          <stop offset="0" stop-color="#cfd2d6"/><stop offset="1" stop-color="#eef0f2"/>
        </linearGradient>
        <linearGradient id="storeGrad" x1="0" y1="0" x2="1" y2="1">
          <stop offset="0" stop-color="#c79a66"/><stop offset="1" stop-color="#6b4a33"/>
        </linearGradient>
      </defs>
      <rect width="654" height="489" fill="url(#paperGrad)"/>
      <polygon points="405,0 620,0 512,106" class="ink-fill"/>
      <polyline points="348,0 442,92 538,0" class="accent-line"/>
      <polygon points="608,38 654,0 654,84" class="ink-line"/>
      <polygon points="555,140 654,40 654,252" class="accent-fill"/>
      <polygon points="310,390 540,142 654,252 654,489 400,489" fill="url(#terminalGrad)" role="img" aria-label="Photo of a bright airport terminal hall with travellers"/>
      <polygon points="430,168 552,290 430,412 308,290" class="ink-line"/>
      <polygon points="200,489 312,380 424,489" class="accent-fill"/>
      <polygon points="265,395 305,435 265,475 225,435" class="ink-fill"/>

      <text x="25" y="49" font-size="40"><tspan class="t-light">Summit Reach </tspan><tspan class="t-bold">Source</tspan></text>
      <text x="25" y="105" font-size="50" class="t-accent">BOOK</text>
      <text x="25" y="155" font-size="46">MARKETING</text>
      <rect x="29" y="169" width="6" height="6" transform="rotate(45 32 172)" class="accent-fill"/>
      <text x="47" y="177" class="t-body">Comprehensive Window Display, Front Table</text>
      <text x="47" y="192" class="t-body">Placement, and Business Center Pockets.</text>
      <rect x="30" y="210" width="6" height="6" transform="rotate(45 33 213)" class="accent-fill"/>
      <text x="48" y="218" class="t-body">45 Airports</text>
      <rect x="120" y="210" width="6" height="6" transform="rotate(45 123 213)" class="accent-fill"/>
      <text x="136" y="218" class="t-body">2 Train Stations</text>
      <rect x="232" y="210" width="6" height="6" transform="rotate(45 235 213)" class="accent-fill"/>
      <text x="248" y="218" class="t-body">80 Bookstores</text>

      <rect x="40" y="305" width="11" height="11" class="accent-fill"/>
      <text x="58" y="316" class="brand">PageLantern</text>

      <polygon points="45,342 61,358 45,374 29,358" class="ink-line" stroke-width="1.5"/>
      <text x="44" y="364" font-size="14" class="t-accent">CONTACT US</text>
      <line x1="44" y1="386" x2="44" y2="470" stroke="#555" stroke-width="1"/>
      <rect x="29" y="390" width="6" height="8" rx="1.5" class="icon"/>
      <text x="51" y="398" class="t-small">1 (555) 014-2290</text>
      <rect x="28" y="414" width="8" height="6" class="icon"/>
      <text x="51" y="422" class="t-small">hello@pagelantern.com</text>
      <circle cx="32" cy="439" r="3.5" class="icon"/>
      <text x="51" y="443" class="t-small">www.pagelantern.com</text>
      <circle cx="32" cy="457" r="2.5" class="icon"/>
      <text x="51" y="463" class="t-small">42 Harbor Lane Riverton</text>
      <text x="51" y="476" class="t-small">NY 10090</text>
    </svg>
  </div>

  <!-- Window display flyer -->
  <div class="flyer flyer--window">
    <svg viewBox="0 0 654 489" xmlns="http://www.w3.org/2000/svg">
      <rect width="654" height="489" fill="url(#paperGrad)"/>
      <polygon points="356,0 542,0 449,92" class="ink-fill"/>
      <polyline points="312,0 392,80 472,0" class="accent-line"/>
      <polygon points="462,140 590,12 654,12 654,230 560,232" fill="url(#storeGrad)" role="img" aria-label="Photo of a bookstore interior with a costumed mascot"/>
      <polygon points="322,232 440,120 570,258 452,376" fill="#9a6e52" role="img" aria-label="Photo of a bookstore window with promotional posters and balloons"/>
      <polygon points="180,395 300,280 418,400 336,489 262,489" fill="url(#storeGrad)" role="img" aria-label="Photo of a bookstore shop front with a book display"/>
      <polygon points="430,400 580,250 654,250 654,489 370,489" fill="#5b4230" role="img" aria-label="Photo of a window display of stacked books"/>
      <polyline points="15,489 85,420 155,489" class="accent-line"/>
      <polygon points="100,489 168,420 236,489" class="ink-fill"/>

      <rect x="24" y="101" width="11" height="11" class="accent-fill"/>
      <text x="42" y="113" class="brand">PageLantern</text>
      <text x="23" y="176" font-size="40"><tspan class="t-light">Windows </tspan><tspan class="t-bold">Display</tspan></text>
      <text x="23" y="213" font-size="27" class="t-accent">OVERVIEW:</text>
      <rect x="30" y="234" width="7" height="7" transform="rotate(45 33 238)" class="accent-fill"/>
      <text x="48" y="244" font-size="16" fill="#333">3 months in 26 bookstores</text>

      <polygon points="38,268 54,284 38,300 22,284" class="ink-line" stroke-width="1.5"/>
      <text x="37" y="290" font-size="14" class="t-accent">CONTACT US</text>
      <line x1="36" y1="316" x2="36" y2="400" stroke="#555" stroke-width="1"/>
      <rect x="21" y="320" width="6" height="8" rx="1.5" class="icon"/>
      <text x="44" y="328" class="t-small">1 (555) 014-2290</text>
      <rect x="20" y="344" width="8" height="6" class="icon"/>
      <text x="44" y="352" class="t-small">hello@pagelantern.com</text>
      <circle cx="24" cy="369" r="3.5" class="icon"/>
      <text x="44" y="373" class="t-small">www.pagelantern.com</text>
      <circle cx="24" cy="387" r="2.5" class="icon"/>
      <text x="44" y="393" class="t-small">42 Harbor Lane Riverton</text>
      <text x="44" y="406" class="t-small">NY 10090</text>
    </svg>
  </div>

  <!-- Front table flyer -->
  <div class="flyer flyer--table">
    <svg viewBox="0 0 654 489" xmlns="http://www.w3.org/2000/svg">
      <rect width="654" height="489" fill="url(#paperGrad)"/>
      <polygon points="358,0 540,0 449,90" class="ink-fill"/>
      <polyline points="312,0 392,80 472,0" class="accent-line"/>
      <polygon points="466,118 590,0 654,0 654,170 560,232" fill="url(#storeGrad)" role="img" aria-label="Photo of a bookstore aisle with a costumed mascot"/>
      <polygon points="322,250 448,132 580,262 452,380" fill="#7a6a8a" role="img" aria-label="Photo of a bookstore table display under a store sign"/>
      <polygon points="184,416 300,280 420,400 370,489 240,489" fill="#3f3a38" role="img" aria-label="Photo of a front table stacked with a featured book"/>
      <polygon points="440,390 580,250 654,250 654,489 400,489" fill="#6e5644" role="img" aria-label="Photo of a wooden table of stacked books"/>
      <polyline points="48,489 102,435 156,489" class="accent-line"/>
      <polygon points="110,489 182,422 254,489" class="ink-fill"/>

      <rect x="24" y="92" width="11" height="11" class="accent-fill"/>
      <text x="42" y="104" class="brand">PageLantern</text>
      <text x="25" y="150" font-size="32" class="t-light">Front Store</text>
      <text x="25" y="195" font-size="40" class="t-bold">Table Display</text>
      <text x="25" y="235" font-size="27" class="t-accent">OVERVIEW:</text>
      <rect x="30" y="254" width="7" height="7" transform="rotate(45 33 258)" class="accent-fill"/>
      <text x="48" y="264" font-size="16" fill="#333">1 month in 26 bookstores</text>

      <polygon points="38,284 54,300 38,316 22,300" class="ink-line" stroke-width="1.5"/>
      <text x="37" y="306" font-size="14" class="t-accent">CONTACT US</text>
      <line x1="36" y1="330" x2="36" y2="414" stroke="#555" stroke-width="1"/>
      <rect x="21" y="334" width="6" height="8" rx="1.5" class="icon"/>
      <text x="44" y="342" class="t-small">1 (555) 014-2290</text>
      <rect x="20" y="358" width="8" height="6" class="icon"/>
      <text x="44" y="366" class="t-small">hello@pagelantern.com</text>
      <circle cx="24" cy="383" r="3.5" class="icon"/>
      <text x="44" y="387" class="t-small">www.pagelantern.com</text>
      <circle cx="24" cy="401" r="2.5" class="icon"/>
      <text x="44" y="407" class="t-small">42 Harbor Lane Riverton</text>
      <text x="44" y="420" class="t-small">NY 10090</text>
    </svg>
  </div>

</div>
</body>
</html>
```